Brightway Haul & Repair Services, are a company that offers a 'one stop shop' pre-move clean up a

I have already selected a logo which I would like on the front of the business cards along with phone numbers, web address and email which are:
0419574302
www.brightwayhaul.com.au
brightwayhaulrepair@mailbox.example

On the back of the card I would like to list some of the types of service we offer (clean - move - repairs/maintenance) which are:
CLEAN - windows, gutters, solar panels, driveways/paths, carpets.
MOVE - Small/medium size house/office moves, large item pick-up & delivery, yard clean-up and removal.
General maintenance and repairs.

I would like the blue logo on a gray background.

Thanks

```html
<!DOCTYPE html>
<html lang="en">
<head>
<meta charset="utf-8">
<title>Brightway Haul &amp; Repair Services – Business Card</title>
<link rel="stylesheet" href="https://fonts.googleapis.com/css2?family=Open+Sans:wght@400;600;700&display=swap">
<style>
  :root {
    --stage: #2b2b2b;
    --card-black: #050505;
    --brand-blue: #2a79c9;
    --brand-blue-deep: #1f63ad;
    --brand-light: #7fb8ea;
    --text-white: #f2f2f2;
  }
  * { box-sizing: border-box; margin: 0; padding: 0; }
  html, body {
    width: 1200px; height: 900px; overflow: hidden;
    background: var(--stage);
    font-family: "Open Sans", Arial, sans-serif;
  }
  .sheet { position: relative; width: 1200px; height: 900px; }

  .card {
    position: absolute; left: 280px;
    width: 640px; height: 366px;
    background: var(--card-black);
    overflow: hidden;
    box-shadow: 0 14px 30px rgba(0,0,0,.45);
  }
  .card--back { top: 62px; }
  .card--front { top: 472px; }

  /* Back: services */
  .back-band {
    position: absolute; left: 0; top: 0; width: 100%; height: 100%;
  }
  .back-name {
    position: absolute; left: 40px; top: 110px;
    font-weight: 700; font-size: 30px; letter-spacing: .5px;
    color: var(--text-white); text-transform: uppercase;
  }
  .services {
    position: absolute; left: 40px; top: 196px; width: 560px;
    font-size: 15px; line-height: 1.55; color: var(--text-white);
  }
  .services .label { color: var(--brand-light); font-weight: 600; }
  .services .highlight { color: var(--brand-light); font-weight: 700; font-size: 16px; }

  /* Front: contact */
  .front-name {
    position: absolute; right: 40px; top: 58px; width: 360px;
    text-align: right;
    font-weight: 700; font-size: 26px; line-height: 1.15;
    color: var(--brand-light); text-transform: uppercase;
  }
  .contact {
    position: absolute; right: 40px; top: 168px;
    list-style: none; text-align: right;
    color: var(--text-white); font-size: 16px; line-height: 1.6;
  }
  .contact li { display: flex; justify-content: flex-end; align-items: center; gap: 10px; }
  .contact .web { color: var(--brand-light); font-size: 18px; }
  .contact .icon { width: 16px; height: 16px; flex: none; }
  .contact .icon-gap { width: 16px; flex: none; }
  .front-band {
    position: absolute; left: 0; bottom: 20px; width: 100%; height: 18px;
    background: var(--brand-blue-deep);
  }
</style>
</head>
<body>
<main class="sheet">

  <section class="card card--back" aria-label="Card back: services">
    <svg class="back-band" viewBox="0 0 640 366" preserveAspectRatio="none" aria-hidden="true">
      <polygon points="0,0 640,0 640,60 0,170" fill="var(--brand-blue)"/>
    </svg>
    <p class="back-name">Brightway Haul</p>
    <p class="services">
      <span class="label">CLEAN</span> - windows, gutters, solar panels, driveways/paths, carpets.<br>
      <span class="label">MOVE</span> - Small/medium size house/office moves, large item pick-up
      &amp; delivery, yard clean-up and removal.<br>
      <span class="highlight">General maintenance and repairs.</span>
    </p>
  </section>

  <section class="card card--front" aria-label="Card front: contact details">
    <h1 class="front-name">Brightway Haul &amp; Repair Services</h1>
    <ul class="contact">
      <li>0419574302
        <svg class="icon" viewBox="0 0 16 16" aria-hidden="true"><rect width="16" height="16" rx="2" fill="var(--brand-blue)"/><path d="M5 3h2l1 3-1.5 1a6 6 0 0 0 2.5 2.5L10 8l3 1v2a1 1 0 0 1-1 1A9 9 0 0 1 4 4a1 1 0 0 1 1-1z" fill="#fff"/></svg>
      </li>
      <li>brightwayhaulrepair@mailbox.example
        <svg class="icon" viewBox="0 0 16 16" aria-hidden="true"><rect x="1" y="3" width="14" height="10" rx="1" fill="var(--brand-blue)"/><path d="M1.5 3.5 8 9l6.5-5.5" stroke="#fff" stroke-width="1.3" fill="none"/></svg>
      </li>
      <li class="web">www.brightwayhaul.com.au
        <svg class="icon" viewBox="0 0 16 16" aria-hidden="true"><circle cx="8" cy="8" r="7" fill="var(--brand-blue)"/><ellipse cx="8" cy="8" rx="3" ry="7" stroke="#fff" fill="none"/><path d="M1 8h14" stroke="#fff"/></svg>
      </li>
    </ul>
    <div class="front-band"></div>
  </section>

</main>
</body>
</html>
```